Bench Advertisement - We Buy Houses Design Needed

Need a catchy, simple but elegant design for bus benches to advertise our company.

We need our website, or phone number, and a smal description (1-2 bulletpoints of what we do and what we offer)

The tricky part is for the designer to fit everything and make the website name as part of the title and fitting everything so that people passing by on the street can see what we offer.

Our website is quickhomebuyerdesk.com - (916) 482-3091

Something simple but something that catches the eye of walking pedestrians, and drivers driving by the bench.

Our company buys houses, any condition, any situation, we buy houses for cash and close quickly. You can use this description to create a few bulletpoints however you like. Must follow dimensions in attachment.

Target Market(s)

People in foreclosure, about to lose their homes, people that need a quick cash sale of their property

Industry/Entity Type

Real Estate

Requirements
Must have
• catchy, website name, phone number, few brief bulletpoints about what we offer, colors that will catch peoples eye while walking or driving - advertisement will be placed on bus benches - visit our website to see the type of houses we buy - Also have more work for winner of design with possible bonuses
Nice to have
• Feel free to use description or images on our website - make sure the description is just bullet points and it fits with the overall theme / size of the advertisement - Bold bright colors - put yourself in their shoes (if you were going through financial difficulties and about to lose your house to foreclosure or auction, what would you want to see to pick up the phone and call us for a quick sale of your house?) (or if you have a house that you are having a problem with, problem renters, unkept/beat up house, what would make you want to call us and sell your house to us?)

```html
<!DOCTYPE html>
<html lang="en">
<head>
<meta charset="utf-8">
<title>Quick Home Buyer Desk – Bench Advertisement</title>
<link href="https://fonts.googleapis.com/css2?family=Open+Sans:wght@400;600;700&family=Fira+Sans+Extra+Condensed:wght@300&display=swap" rel="stylesheet">
<style>
  :root {
    --page-bg: #1f1f1f;
    --bench-white: #ffffff;
    --teal: #3f8f9c;
    --teal-light: #74b6c0;
    --teal-dark: #3a8593;
    --grey-text: #6b6b6b;
    --on-teal: #ffffff;
  }
  * { margin: 0; padding: 0; box-sizing: border-box; }
  html, body {
    width: 1200px; height: 768px; overflow: hidden;
    background: var(--page-bg);
  }
  .bench-ad {
    position: absolute; left: 50px; top: 231px;
    width: 1100px; height: 305px;
    background: var(--bench-white);
    overflow: hidden;
    font-family: "Open Sans", Arial, sans-serif;
  }
  .feature-panel { position: absolute; left: 0; top: 0; width: 531px; height: 305px; }
  .steps {
    position: absolute; left: 23px; top: 13px;
    color: var(--on-teal);
  }
  .steps-title { font-size: 18px; font-weight: 600; letter-spacing: 0.2px; line-height: 24px; margin-bottom: 2px; }
  .steps-list { list-style: none; }
  .steps-list li {
    display: flex; align-items: center; gap: 6px;
    font-size: 11.5px; line-height: 18px;
  }
  .step-marker {
    width: 13px; height: 13px; border: 1.3px solid var(--on-teal); border-radius: 50%;
    display: inline-block;
  }
  .contact {
    position: absolute; right: 38px; top: 0; width: 560px; height: 305px;
    text-align: right; color: var(--teal);
  }
  .contact > * { position: absolute; right: 0; white-space: nowrap; }
  .brand-name {
    top: 96px;
    display: flex; align-items: center; gap: 8px;
    font-size: 20.5px; font-weight: 400; line-height: 26px; letter-spacing: 0.2px;
  }
  .brand-square { width: 14px; height: 14px; background: var(--teal); }
  .phone { top: 136px; font-size: 40px; font-weight: 700; line-height: 44px; }
  .website { top: 179px; font-size: 21px; font-weight: 600; line-height: 24px; letter-spacing: 0.1px; }
  .offer-list { list-style: none; top: 213px; }
  .offer-list li {
    display: flex; align-items: center; justify-content: flex-end; gap: 10px;
    font-family: "Fira Sans Extra Condensed", "Arial Narrow", sans-serif;
    font-weight: 300; font-size: 24px; line-height: 35px;
    color: var(--grey-text);
  }
  .offer-icon { width: 17px; height: 17px; flex: none; }
</style>
</head>
<body>
  <section class="bench-ad">
    <svg class="feature-panel" viewBox="0 0 531 305">
      <defs>
        <linearGradient id="panelGradient" x1="0" y1="0" x2="0" y2="1">
          <stop offset="0" stop-color="#74b6c0"/>
          <stop offset="1" stop-color="#3a8593"/>
        </linearGradient>
        <linearGradient id="sceneGradient" x1="0" y1="1" x2="1" y2="0">
          <stop offset="0" stop-color="#ffffff" stop-opacity="0.45"/>
          <stop offset="0.55" stop-color="#ffffff" stop-opacity="0.18"/>
          <stop offset="1" stop-color="#ffffff" stop-opacity="0"/>
        </linearGradient>
      </defs>
      <polygon points="0,0 382,0 531,305 0,305" fill="url(#panelGradient)"/>
      <polygon points="0,90 426,90 531,305 0,305" fill="url(#sceneGradient)"
        role="img" aria-label="Illustration of white and teal house rooftops with a check mark"/>
    </svg>

    <div class="steps">
      <h2 class="steps-title">WE MAKE IT SIMPLE</h2>
      <ul class="steps-list">
        <li><span class="step-marker"></span>Fill Out The Form</li>
        <li><span class="step-marker"></span>We’ll Call You Within A Few Hours</li>
        <li><span class="step-marker"></span>We Work With You On A Solution</li>
        <li><span class="step-marker"></span>Move On With Your Life</li>
      </ul>
    </div>

    <div class="contact">
      <div class="brand-name"><span class="brand-square"></span>QUICK HOME BUYER DESK</div>
      <p class="phone">Cell (916) 482-3091</p>
      <p class="website">WWW.QUICKHOMEBUYERDESK.COM</p>
      <ul class="offer-list">
        <li>Our company buys houses, any condition, any situation
          <svg class="offer-icon" viewBox="0 0 17 17"><g fill="#3f8f9c"><rect x="0" y="0" width="7" height="7"/><rect x="10" y="0" width="7" height="7"/><rect x="0" y="10" width="7" height="7"/><rect x="10" y="10" width="7" height="7"/></g></svg>
        </li>
        <li>We buy houses for cash &amp; close quickly
          <svg class="offer-icon" viewBox="0 0 17 17"><g fill="#3f8f9c"><rect x="0" y="0" width="7" height="7"/><rect x="10" y="0" width="7" height="7"/><rect x="0" y="10" width="7" height="7"/><rect x="10" y="10" width="7" height="7"/></g></svg>
        </li>
      </ul>
    </div>
  </section>
</body>
</html>
```